BRACKENRIDGE BUILDERS B-Card

I currently have a b-card design but will be removing the image (tree) from the logo and have text only.
I want the card to be classy and strong within the building and construction industry.
I will be using Spot UV on the cards as per the attached examples. I will also send through some sketched ideas that I have in mind.
The color blue is similar to the image (No. 6) attached images

Target Market(s)

middle to maturre aged.
Home Owners / Renovators and Builders

Industry/Entity Type

Construction

Contact Information for Business Card

BRACKENRIDGE BUILDERS
Name: Dermot Quaile
Title: Project Manager
Mobile: 0412 537 804
Office: (08) 9173 5842
Address: 17C Pellworth Avenue, Tarrowby WA 6071
Email: info@brackenridgebuild.com.au
PO Box: 3817 Tarrowby WA 6957

Colors
0592cd
33a6d7
85cae6
1b1b1b

Requirements
Must have
• 1. It must have spot UV on the front of card, maybe back of card too
• 2. I really like the blue on image 6. (or at least a really cool electric blue against the charcoal grey background)
• 3. The font must be slimline and modern. Easy to read
• 4. There must be no black used on the card... Only greys and dark charcoal greys
• 5. Use only the text from the logo "Brackenridge Builders" Not the image of the tree. I am wanting the b-cards to be more masculine.
Nice to have
• 1. I like the design concept on image 6. but happy to see what else you can do with the Spot UV
• 2. Unless you have a really cool idea of the image of the tree (from previous logo) Spot UV somewhere in the design concept thats original and different then I am keen to see what you come up with
• 3. Try changing the color of the logo eg. full white or Blue and white
• 4. Another option is to have the Brackenridge Logo on the front of card with the spot UV in the background of text which we specialise in eg, Roofing, Ceiling, Insulation, Gutter Guards, Electrical, Insurance etc and we can add or reduce items as required. Similar to image 12.
Should not have
• Do not include the image of the tree from previous logo. unless you have a really cool idea of Spot UV somewhere in the design concept thats original and different.

```html
<!DOCTYPE html>
<html lang="en">
<head>
<meta charset="utf-8">
<title>Brackenridge Builders – Business Card</title>
<link rel="stylesheet" href="https://fonts.googleapis.com/css2?family=Open+Sans:wght@400;600&display=swap">
<style>
  :root {
    --backdrop: #4a4039;
    --card: #272727;
    --card-shade: #2e2e2e;
    --uv-light: #3a3a3a;
    --uv-dark: #1e1e1e;
    --blue: #33a6d7;
    --white: #f2f2f2;
  }
  * { margin: 0; padding: 0; box-sizing: border-box; }
  html, body {
    width: 1200px; height: 1000px; overflow: hidden;
    background: var(--backdrop);
    font-family: "Open Sans", Arial, sans-serif;
  }
  .canvas { position: relative; width: 1200px; height: 1000px; }
  .card {
    position: absolute; left: 265px; width: 665px;
    background: var(--card);
    box-shadow: 0 6px 14px rgba(20, 14, 10, 0.45);
  }
  .card--front { top: 73px; height: 397px; }
  .card--back { top: 533px; height: 395px; overflow: hidden; }

  .business-name {
    color: var(--blue); font-weight: 600; line-height: 1;
    white-space: nowrap;
  }
  .card--front .business-name {
    position: absolute; right: 32px; top: 92px;
    font-size: 30px; text-align: right;
  }

  .contact { position: absolute; left: 33px; top: 176px; color: var(--white); }
  .contact__name { color: var(--blue); font-size: 19px; font-weight: 600; line-height: 1.2; }
  .contact__title { font-size: 16px; line-height: 1.3; }
  .contact__list { list-style: none; margin-top: 17px; }
  .contact__list li { display: flex; align-items: center; font-size: 15.5px; height: 23px; }
  .contact__list svg { width: 14px; height: 14px; margin-right: 9px; fill: var(--blue); flex: none; }
  .contact__address { margin-top: 8px; font-size: 15.5px; line-height: 27px; }

  .uv-art {
    position: absolute; left: 0; top: 0; width: 100%; height: 100%;
    background: radial-gradient(ellipse 48% 62% at 50% 55%, var(--uv-light) 0%, var(--card-shade) 55%, var(--card) 80%),
                linear-gradient(90deg, transparent 60%, var(--uv-dark) 100%);
  }
  .card--back .business-name {
    position: absolute; left: 0; right: 0; top: 180px;
    font-size: 38px; text-align: center;
  }
</style>
</head>
<body>
<div class="canvas">
  <section class="card card--front">
    <p class="business-name">Brackenridge Builders</p>
    <div class="contact">
      <p class="contact__name">DERMOT QUAILE</p>
      <p class="contact__title">Project Manager</p>
      <ul class="contact__list">
        <li><svg viewBox="0 0 14 14" aria-hidden="true"><path d="M4 0h6a1 1 0 0 1 1 1v12a1 1 0 0 1-1 1H4a1 1 0 0 1-1-1V1a1 1 0 0 1 1-1zm.5 1.5v10h5v-10z"/></svg>0412 537 804</li>
        <li><svg viewBox="0 0 14 14" aria-hidden="true"><path d="M1 4c0-1.5 3-3 6-3s6 1.5 6 3v1.5h-3V4H4v1.5H1zM3 7l2-2h4l2 2v5H3z"/></svg>(08) 9173 5842</li>
        <li><svg viewBox="0 0 14 14" aria-hidden="true"><path d="M0 3h14v1L7 8 0 4zM0 5.3l7 4 7-4V11H0z"/></svg>info@brackenridgebuild.com.au</li>
      </ul>
      <p class="contact__address">PO Box 3817 Tarrowby WA 6957<br>17C Pellworth Avenue, Tarrowby WA 6071</p>
    </div>
  </section>

  <section class="card card--back">
    <div class="uv-art" role="img" aria-label="Spot UV illustration of a broad leafy tree spreading behind the name"></div>
    <p class="business-name">Brackenridge Builders</p>
  </section>
</div>
</body>
</html>
```